HIgh-end jewelry designer needs a business card design

I need a business card design for the ecclectic & rather expensive jewelry designs. My approach to my work is to combine very old jewelry offset with contemporary items. I enjoy the idea of legacy as well as repurposing finely crafted items that are not possible to create any longer. My desire is to celebrate the past in a contemporary & funky way. The name of my business is VELLORINE. I see my business card design as simple & yet enigmatic as possible. In the end... clean, simple & understated is the look I am after. Thank you for your consideration...

Target Market(s)

I will use this business card for the trade as well as customers

Industry/Entity Type

Business

Contact Information for Business Card

Marta Quorrin Owner/Designer 555-203-7718

Requirements
Must have
• Clean & simple sophisticated design using the word "Vellorinne" as the logo. I like the idea of a play on the word itself, perhaps even using different fonts (i.e.: a bold helvetica combined with a lovely script). I'm afraid to say more because I don't want to limit creative input. Gosh, sometimes it's ok to break the rules!
Nice to have
• In my mind, I have imagined this business card to be simple, using my company name "Vellorine" in a playful yet sophisticated manner. I believe that doing something beautifully simple can be a true challenge. I have imagined something with just black & white, however I am open to ideas... after all that's why I'm here!
Should not have
• As Mozart once said... "It has too many notes!" I know I'm being silly, but I don't want it to be complicated or overly ornate.

```html
<!DOCTYPE html>
<html lang="en">
<head>
<meta charset="utf-8">
<title>Vellorine — Business Card</title>
<link rel="stylesheet" href="https://fonts.googleapis.com/css2?family=Poiret+One&family=Great+Vibes&display=swap">
<style>
  :root {
    --page-bg: #e9dfc6;
    --card-bg: #2f2b35;
    --card-glow: #35303c;
    --logo-ink: #f4f2f6;
    --name-ink: #c9c5cf;
    --role-ink: #6e6975;
    --phone-ink: #8b8692;
    --chain: #cfccd4;
  }
  * { margin: 0; padding: 0; box-sizing: border-box; }
  html, body {
    width: 800px;
    height: 1200px;
    overflow: hidden;
    background: var(--page-bg);
  }
  .canvas {
    position: relative;
    width: 800px;
    height: 1200px;
  }
  .card {
    position: absolute;
    left: 100px;
    top: 60px;
    width: 600px;
    height: 1080px;
    background: radial-gradient(ellipse at 45% 55%, var(--card-glow) 0%, var(--card-bg) 60%);
    overflow: hidden;
  }
  .card__divider {
    position: absolute;
    inset: 0;
    width: 600px;
    height: 1080px;
  }
  .card__text {
    position: absolute;
    white-space: nowrap;
    transform: translate(-50%, -50%) rotate(-61deg);
  }
  .brand-name {
    left: 193px;
    top: 198px;
    font-family: "Poiret One", sans-serif;
    font-size: 44px;
    letter-spacing: 8px;
    color: var(--logo-ink);
  }
  .owner-name {
    left: 239px;
    top: 549px;
    font-family: "Great Vibes", cursive;
    font-size: 34px;
    color: var(--name-ink);
  }
  .owner-role {
    left: 351px;
    top: 539px;
    font-family: "Poiret One", sans-serif;
    font-size: 19px;
    letter-spacing: 2px;
    color: var(--role-ink);
  }
  .owner-phone {
    left: 498px;
    top: 955px;
    font-family: "Poiret One", sans-serif;
    font-size: 23px;
    letter-spacing: 2px;
    color: var(--phone-ink);
  }
</style>
</head>
<body>
  <main class="canvas">
    <section class="card">
      <svg class="card__divider" viewBox="0 0 600 1080" aria-hidden="true">
        <line x1="0" y1="1080" x2="600" y2="0" stroke="var(--chain)" stroke-width="2" stroke-dasharray="3 1.5"/>
      </svg>
      <h1 class="card__text brand-name">VELLORINE</h1>
      <p class="card__text owner-name">Marta Quorrin</p>
      <p class="card__text owner-role">Owner-Designer</p>
      <p class="card__text owner-phone">555-203-7718</p>
    </section>
  </main>
</body>
</html>
```